Financial Services General Marketing Brochure

Need a brochure to help recipients understand what makes BHC unique and the services that we offer. Must match look/feel of website https://brightharborcollective.com Layouts should make it easy to read the content - content should not be crammed into a traditional size/layout. Please see attached creative brief for specifics.

Target Market(s)

Financial advisors and mature couples looking for trustee services.

Industry/Entity Type

Financial Service

Colors
34a7d8
ffc214

Requirements
Must have
• See Creative Brief

```html
<!DOCTYPE html>
<html lang="en">
<head>
<meta charset="utf-8">
<title>Bright Harbor Collective – Brochure</title>
<link href="https://fonts.googleapis.com/css2?family=Montserrat:wght@500;600;700&family=Merriweather+Sans:wght@700;800&display=swap" rel="stylesheet">
<style>
  :root{
    --stage:#e6e6e6;
    --slate:#5d87b3;
    --slate-deep:#3f6a96;
    --navy:#2f5577;
    --gold:#e8a92a;
    --amber:#f5a623;
    --orange:#ea7b1e;
    --cream:#f6ede0;
    --sand:#d9cfc4;
    --white:#ffffff;
  }
  *{box-sizing:border-box;margin:0;padding:0}
  html,body{width:1200px;height:1200px;overflow:hidden;background:var(--stage)}
  body{position:relative;font-family:"Montserrat",sans-serif}
  .spread{position:absolute;left:60px;width:1080px;height:520px;display:flex;box-shadow:0 14px 30px rgba(0,0,0,.18)}
  .spread--inside{top:50px}
  .spread--outside{top:630px}
  .panel{position:relative;width:540px;height:520px;overflow:hidden}

  /* inside spread */
  .specialties{background:var(--slate)}
  .specialties__tab{position:absolute;left:30px;top:38px;width:218px;height:34px;background:var(--gold);color:var(--white);font-weight:700;font-size:19px;line-height:34px;padding-left:14px}
  .specialties__intro{position:absolute;left:30px;top:82px;width:215px;color:var(--gold);font-size:12px;font-weight:600;line-height:15px}
  .specialties__list{position:absolute;left:30px;top:126px;list-style:none}
  .specialties__list li{color:var(--white);font-size:15px;font-weight:600;height:25px;display:flex;align-items:center}
  .specialties__list li::before{content:"";width:11px;height:11px;border-radius:50%;background:var(--gold);margin-right:10px}
  .specialties__frame{position:absolute;left:210px;top:268px;width:237px;height:190px;background:var(--gold)}
  .specialties__photo{position:absolute;left:240px;top:10px;width:300px;height:420px;background:linear-gradient(160deg,#6f6a3a 0%,#8a6a3a 45%,#a4774a 75%,#6e4a2e 100%)}

  .cover{background:linear-gradient(180deg,#6b92bb 0%,var(--slate) 60%,#547fac 100%)}
  .cover__brand{position:absolute;left:150px;top:270px;width:340px;text-align:center;color:var(--amber);font-family:"Merriweather Sans",sans-serif;font-weight:800;font-size:38px;line-height:44px}
  .cover__dot{display:block;width:64px;height:64px;border-radius:50%;background:var(--amber);margin:0 auto 18px}

  /* outside spread */
  .front__photo{position:absolute;left:0;top:0;width:540px;height:320px;background:linear-gradient(180deg,#c9b98a 0%,#8e8a5e 40%,#6b7f8e 75%,#4e6d92 100%)}
  .front__brand{position:absolute;left:0;top:320px;width:186px;height:200px;background:var(--cream);display:flex;flex-direction:column;align-items:center;justify-content:center;text-align:center;color:var(--navy);font-family:"Merriweather Sans",sans-serif;font-weight:800;font-size:23px;line-height:28px}
  .front__brand .mark{width:44px;height:44px;border-radius:50%;background:var(--amber);margin-bottom:14px}
  .front__headline{position:absolute;left:186px;top:320px;width:354px;height:200px;background:linear-gradient(180deg,var(--orange) 0%,var(--amber) 100%);color:var(--white);font-family:"Merriweather Sans",sans-serif;font-weight:700;text-align:center;display:flex;flex-direction:column;justify-content:center}
  .front__headline span{display:block;font-size:27px;line-height:40px}
  .front__headline .big{font-size:40px;line-height:52px}

  .back{background:linear-gradient(180deg,var(--sand) 0%,var(--sand) 50%,var(--orange) 50%,#d79a2c 100%)}
  .back__brand{position:absolute;left:0;top:52px;width:540px;display:flex;align-items:center;justify-content:center;gap:14px;color:var(--navy);font-family:"Merriweather Sans",sans-serif;font-weight:800;font-size:26px;line-height:30px}
  .back__brand .mark{width:58px;height:58px;border-radius:50%;background:var(--amber)}
  .back__photo{position:absolute;left:50px;top:160px;width:440px;height:220px;background:linear-gradient(180deg,#4f7396 0%,#3d6187 100%)}
  .back__phone{position:absolute;left:170px;top:243px;width:200px;height:68px;border:3px solid var(--white);color:var(--white);font-size:19px;font-weight:600;display:flex;align-items:center;justify-content:center;gap:8px}
  .contact{position:absolute;left:0;width:540px;text-align:center;color:var(--white)}
  .contact__label{font-size:14px;font-weight:600;display:flex;align-items:center;justify-content:center;gap:6px}
  .contact__rule{width:116px;height:3px;background:var(--white);margin:5px auto 9px}
  .contact__value{font-size:18px;font-weight:600}
  .contact--email{top:403px}
  .contact--web{top:463px}
</style>
</head>
<body>

<section class="spread spread--inside">
  <div class="panel specialties">
    <div class="specialties__tab">Trust Specialties</div>
    <p class="specialties__intro">The general types of trusts on which we serve as trustee:</p>
    <ul class="specialties__list">
      <li>Family Trusts</li>
      <li>Charitable Trusts</li>
      <li>Family Foundations</li>
      <li>Life Insurance Trusts</li>
      <li>Retirement Trusts</li>
      <li>Special Needs Trusts</li>
    </ul>
    <div class="specialties__frame"></div>
    <div class="specialties__photo" role="img" aria-label="Photo of a parent and children playing piggyback in a sunlit pine forest"></div>
  </div>
  <div class="panel cover" role="img" aria-label="Faded blue-tinted photo of a family playing tug of war outdoors">
    <div class="cover__brand"><span class="cover__dot"></span>Bright Harbor<br>Collective</div>
  </div>
</section>

<section class="spread spread--outside">
  <div class="panel front">
    <div class="front__photo" role="img" aria-label="Photo of a smiling three-generation family outdoors"></div>
    <div class="front__brand"><span class="mark"></span>Bright<br>Harbor<br>Collective</div>
    <h1 class="front__headline">
      <span>Helping Families</span>
      <span>Protect and Enrich</span>
      <span>a Multi-Generational</span>
      <span class="big">Heritage</span>
    </h1>
  </div>
  <div class="panel back">
    <div class="back__brand"><span class="mark"></span><span>Bright Harbor<br>Collective</span></div>
    <div class="back__photo" role="img" aria-label="Blue-tinted photo of a family walking in silhouette"></div>
    <div class="back__phone">
      <svg width="16" height="16" viewBox="0 0 24 24" aria-hidden="true"><path fill="#fff" d="M6.6 10.8a15 15 0 0 0 6.6 6.6l2.2-2.2a1 1 0 0 1 1-.25 11.4 11.4 0 0 0 3.6.57 1 1 0 0 1 1 1V20a1 1 0 0 1-1 1A17 17 0 0 1 3 4a1 1 0 0 1 1-1h3.5a1 1 0 0 1 1 1 11.4 11.4 0 0 0 .57 3.6 1 1 0 0 1-.25 1z"/></svg>
      555-014-2290
    </div>
    <div class="contact contact--email">
      <div class="contact__label">
        <svg width="14" height="11" viewBox="0 0 14 11" aria-hidden="true"><rect width="14" height="11" rx="1" fill="#fff"/><path d="M1 1l6 5 6-5" stroke="#e08a24" stroke-width="1.4" fill="none"/></svg>
        Email
      </div>
      <div class="contact__rule"></div>
      <div class="contact__value">info@brightharborcollective.com</div>
    </div>
    <div class="contact contact--web">
      <div class="contact__label">
        <svg width="13" height="13" viewBox="0 0 14 14" aria-hidden="true"><g fill="none" stroke="#fff" stroke-width="1.3"><circle cx="7" cy="7" r="6"/><ellipse cx="7" cy="7" rx="2.6" ry="6"/><path d="M1 7h12"/></g></svg>
        Website
      </div>
      <div class="contact__rule"></div>
      <div class="contact__value">brightharborcollective.com</div>
    </div>
  </div>
</section>

</body>
</html>
```